Kickgrid Numbers Service

We have a football stats service that we feel would benefit from some design input. In particular we would like the designer to look at three pages. We will then transfer this style across the rest of the site.

We are looking for designs for three pages. Links to the existing pages we would like reworked are:

Player:
http://demostats.kickgrid-example.com/Player.asp?lang=&coid=4&teid=220&plid=197404

Team Stats:
http://demostats.kickgrid-example.com/Team_Stats.asp?lang=&coid=4&teid=218

League Table:
http://demostats.kickgrid-example.com/Comp_Table.asp?lang=&coid=4

We require the page structure to remain as is with the main country/competition selector on the left and the content on the right.

The colour palette, fonts, content separators etc are all in your hands. We will use this version as a sales tool for our services. In many cases this will be restyled to match a specific clients requirements.

We are happy for this to be done in HTML/CSS or as a layered image file.

Target Market(s)

These stats pages are for use on newspaper and bookmaker websites.

Industry/Entity Type

Sales

Requirements
Nice to have
• A nice colour palette for graphs and charts is important.

```html
<!DOCTYPE html>
<html lang="en">
<head>
<meta charset="utf-8">
<title>Kickgrid Numbers Service – Player</title>
<link href="https://fonts.googleapis.com/css2?family=Open+Sans:wght@400;600;700&display=swap" rel="stylesheet">
<style>
:root{
  --sidebar:#1f2430;
  --sidebar-text:#ffffff;
  --sidebar-muted:#8c919b;
  --accent:#3f88c8;
  --page:#e8e9eb;
  --card:#ffffff;
  --text:#3b3e44;
  --heading:#4a4d52;
  --rule:#dcdde0;
  --tabbar:#1f2533;
  --apps-fill:#93d9c9;
  --apps-line:#5ec7af;
  --goals-fill:#5cbbd9;
  --goals-line:#3ea6d3;
  --pitch-dark:#2f4a2a;
  --pitch-light:#5d7d4e;
}
*{box-sizing:border-box;margin:0;padding:0}
html,body{width:1200px;height:767px;overflow:hidden}
body{font-family:"Open Sans",Arial,sans-serif;background:var(--page);color:var(--text);position:relative;font-size:13px}

.brand{position:absolute;left:0;top:0;width:235px;height:47px;background:#fff;display:flex;align-items:center;justify-content:center;font-size:16px;font-weight:400;color:#2b2e33;letter-spacing:.2px;border-right:1px solid var(--rule)}
.topbar{position:absolute;left:235px;top:0;right:0;height:47px;background:#fff;border-bottom:1px solid var(--rule)}
.menu-toggle{position:absolute;left:18px;top:17px}
.top-search{position:absolute;left:635px;top:11px;width:167px;height:25px;border:1px solid #c9cbcf;border-radius:13px;font-size:11px;color:#9a9da3;padding:5px 10px}
.top-search svg{position:absolute;right:9px;top:6px}
.user{position:absolute;left:832px;top:9px;display:flex;align-items:center;gap:4px;font-size:13px;color:#2b2e33}
.user-photo{width:29px;height:29px;border-radius:50%;background:#4a4a4a}

.sidebar{position:absolute;left:0;top:47px;width:235px;bottom:0;background:var(--sidebar);color:var(--sidebar-text)}
.date{position:absolute;left:19px;top:25px;display:flex;align-items:center;gap:11px;font-size:17px}
.label{position:absolute;left:19px;font-size:12px;font-weight:600;color:var(--sidebar-muted)}
.side-search{position:absolute;left:12px;top:93px;width:211px;height:25px;background:#fff;border-radius:13px;font-size:11px;color:#9a9da3;padding:5px 11px}
.side-search svg{position:absolute;right:11px;top:6px}
.nav-active{position:absolute;left:10px;top:173px;width:215px;height:37px;background:var(--accent);border-radius:3px;font-size:12.5px;padding:10px 9px;display:flex;justify-content:space-between;align-items:center}
.countries{position:absolute;left:30px;top:218px;width:185px;list-style:none}
.countries li{height:32.5px;display:flex;align-items:center;font-size:12.5px}
.countries li .arrow{margin-right:9px}
.countries li svg.flag{margin-left:auto}
.nav-continental{position:absolute;left:19px;top:437px;width:197px;font-size:12.5px;display:flex;justify-content:space-between;align-items:center}

.card{position:absolute;background:var(--card);border-radius:3px;box-shadow:0 1px 2px rgba(0,0,0,.08)}
.profile{left:260px;top:72px;width:859px;height:330px}
.player-photo{position:absolute;left:125px;top:15px;width:126px;height:126px;border-radius:50%;background:radial-gradient(circle at 50% 45%,#c79a7e 0,#a47659 35%,#3e4c6a 70%,#2a3550 100%)}
.player-head{position:absolute;left:375px;top:24px}
.player-name{font-size:23px;font-weight:400;color:var(--heading);margin-bottom:6px}
.club{display:flex;align-items:center;gap:6px;font-size:15.5px;margin-bottom:6px}
.facts{font-size:12.5px;line-height:19px}
.facts b{font-weight:700}
.profile hr{position:absolute;left:0;right:0;top:166px;border:0;border-top:1px solid var(--rule)}
.detail{position:absolute;font-size:12.5px;line-height:18px}
.detail dt{font-weight:700}
.detail dd{display:flex;align-items:center;gap:5px}
.pitch{position:absolute;left:449px;top:207px;width:348px;height:103px;background:linear-gradient(180deg,var(--pitch-light),var(--pitch-dark));clip-path:polygon(8% 0,92% 0,100% 100%,0 100%)}

.stats{left:260px;top:428px;width:859px;height:320px;overflow:hidden}
.tabs{height:44px;background:var(--tabbar);display:flex;border-radius:3px 3px 0 0}
.tab{width:112px;display:flex;align-items:center;justify-content:center;color:#fff;font-size:12.5px}
.tab.active{background:#fff;color:var(--text);width:78px;border-radius:3px 3px 0 0}
.chart{position:absolute;left:21px;top:54px;width:805px;height:259px;border:1px solid #dfe0e3;border-bottom:0}
.legend{position:absolute;left:5px;top:8px;font-size:8.5px;font-family:Arial,sans-serif;color:#333;line-height:15px}
.legend span{display:inline-block;width:10px;height:10px;vertical-align:-2px;margin-right:2px}
</style>
</head>
<body>

<div class="brand">Kickgrid STATS</div>
<header class="topbar">
  <svg class="menu-toggle" width="15" height="13" viewBox="0 0 15 13"><rect y="0" width="15" height="2" fill="#222"/><rect y="5.5" width="15" height="2" fill="#222"/><rect y="11" width="15" height="2" fill="#222"/></svg>
  <div class="top-search">Search ...
    <svg width="11" height="11" viewBox="0 0 11 11"><circle cx="4.5" cy="4.5" r="3.5" stroke="#555" stroke-width="1.6" fill="none"/><line x1="7" y1="7" x2="10" y2="10" stroke="#555" stroke-width="1.8"/></svg>
  </div>
  <div class="user"><div class="user-photo" role="img" aria-label="User profile photo"></div>Aaron Kessel
    <svg width="8" height="5" viewBox="0 0 8 5"><path d="M0 0h8L4 5z" fill="#333"/></svg></div>
</header>

<nav class="sidebar">
  <div class="date">
    <svg width="17" height="17" viewBox="0 0 17 17"><rect x="1" y="3" width="15" height="13" fill="none" stroke="#fff" stroke-width="1.6"/><rect x="1" y="3" width="15" height="3" fill="#fff"/><rect x="4" y="0.5" width="2" height="4" fill="#fff"/><rect x="11" y="0.5" width="2" height="4" fill="#fff"/><g fill="#fff"><rect x="4" y="8" width="2" height="2"/><rect x="7.5" y="8" width="2" height="2"/><rect x="11" y="8" width="2" height="2"/><rect x="4" y="11.5" width="2" height="2"/><rect x="7.5" y="11.5" width="2" height="2"/><rect x="11" y="11.5" width="2" height="2"/></g></svg>
    25 September 2014
  </div>
  <div class="label" style="top:68px">Search</div>
  <div class="side-search">Search ...
    <svg width="11" height="11" viewBox="0 0 11 11"><circle cx="4.5" cy="4.5" r="3.5" stroke="#333" stroke-width="1.6" fill="none"/><line x1="7" y1="7" x2="10" y2="10" stroke="#333" stroke-width="1.8"/></svg>
  </div>
  <div class="label" style="top:155px">Domestic Football</div>
  <div class="nav-active">Domestic Football
    <svg width="10" height="7" viewBox="0 0 10 7"><path d="M1 1l4 4 4-4" stroke="#fff" stroke-width="1.6" fill="none"/></svg></div>
  <ul class="countries">
    <li><svg class="arrow" width="4" height="7" viewBox="0 0 4 7"><path d="M0 0l4 3.5L0 7z" fill="#fff"/></svg>England
      <svg class="flag" width="27" height="16" viewBox="0 0 27 16"><rect width="27" height="16" fill="#fff"/><rect x="11.5" width="4" height="16" fill="#d2232a"/><rect y="6" width="27" height="4" fill="#d2232a"/></svg></li>
    <li><svg class="arrow" width="4" height="7" viewBox="0 0 4 7"><path d="M0 0l4 3.5L0 7z" fill="#fff"/></svg>Scotland
      <svg class="flag" width="27" height="16" viewBox="0 0 27 16"><rect width="27" height="16" fill="#1f4fa3"/><path d="M0 0L27 16M27 0L0 16" stroke="#fff" stroke-width="2.6"/></svg></li>
    <li><svg class="arrow" width="4" height="7" viewBox="0 0 4 7"><path d="M0 0l4 3.5L0 7z" fill="#fff"/></svg>Spain
      <svg class="flag" width="27" height="16" viewBox="0 0 27 16"><rect width="27" height="16" fill="#c8102e"/><rect y="4" width="27" height="8" fill="#f5c400"/></svg></li>
    <li><svg class="arrow" width="4" height="7" viewBox="0 0 4 7"><path d="M0 0l4 3.5L0 7z" fill="#fff"/></svg>Italy
      <svg class="flag" width="27" height="16" viewBox="0 0 27 16"><rect width="9" height="16" fill="#1a9b47"/><rect x="9" width="9" height="16" fill="#fff"/><rect x="18" width="9" height="16" fill="#d2232a"/></svg></li>
    <li><svg class="arrow" width="4" height="7" viewBox="0 0 4 7"><path d="M0 0l4 3.5L0 7z" fill="#fff"/></svg>Germany
      <svg class="flag" width="27" height="16" viewBox="0 0 27 16"><rect width="27" height="5.4" fill="#111"/><rect y="5.3" width="27" height="5.4" fill="#d2232a"/><rect y="10.6" width="27" height="5.4" fill="#f5c400"/></svg></li>
    <li><svg class="arrow" width="4" height="7" viewBox="0 0 4 7"><path d="M0 0l4 3.5L0 7z" fill="#fff"/></svg>France
      <svg class="flag" width="27" height="16" viewBox="0 0 27 16"><rect width="9" height="16" fill="#2a3fbf"/><rect x="9" width="9" height="16" fill="#fff"/><rect x="18" width="9" height="16" fill="#d2232a"/></svg></li>
  </ul>
  <div class="nav-continental">Continental Football
    <svg width="6" height="10" viewBox="0 0 6 10"><path d="M1 1l4 4-4 4" stroke="#fff" stroke-width="1.6" fill="none"/></svg></div>
</nav>

<main>
  <section class="card profile">
    <div class="player-photo" role="img" aria-label="Player portrait photo"></div>
    <div class="player-head">
      <h1 class="player-name">Milan Radovanic</h1>
      <div class="club"><svg width="26" height="15" viewBox="0 0 26 15"><rect width="26" height="15" fill="#fff" stroke="#ddd"/><rect x="11" width="4" height="15" fill="#d2232a"/><rect y="5.5" width="26" height="4" fill="#d2232a"/></svg>Westbridge</div>
      <div class="facts">
        <div><b>Position:</b> Defender</div>
        <div><b>Date of Birth:</b> 14/06/1984</div>
        <div><b>Age:</b> 30</div>
      </div>
    </div>
    <hr>
    <dl class="detail" style="left:29px;top:190px"><dt>Height</dt><dd>1.85 m / 6 ft 1 in</dd></dl>
    <dl class="detail" style="left:29px;top:244px"><dt>Weight</dt><dd>83 kg /13 st 1 lbs</dd></dl>
    <dl class="detail" style="left:236px;top:190px"><dt>Place of Birth</dt><dd>Novi Dvorac, Serbia</dd></dl>
    <dl class="detail" style="left:236px;top:244px"><dt>Nationality</dt><dd><svg width="26" height="15" viewBox="0 0 26 15"><rect width="26" height="5" fill="#c8233a"/><rect y="5" width="26" height="5" fill="#2b4a9c"/><rect y="10" width="26" height="5" fill="#fff"/></svg>Serbia</dd></dl>
    <div class="pitch" role="img" aria-label="Football pitch showing the player's position"></div>
  </section>

  <section class="card stats">
    <div class="tabs">
      <div class="tab">This Season</div>
      <div class="tab active">Career</div>
    </div>
    <div class="chart">
      <svg width="805" height="259" viewBox="0 0 823 264" preserveAspectRatio="none">
        <g stroke="#e6e7ea" stroke-width="1">
          <line x1="0" y1="44" x2="823" y2="44"/><line x1="0" y1="88" x2="823" y2="88"/><line x1="0" y1="132" x2="823" y2="132"/>
        </g>
        <path d="M0 150L117 167L235 167L352 150L470 106L587 88L704 97L822 71L822 264L0 264Z" fill="var(--apps-fill)"/>
        <polyline points="0,150 117,167 235,167 352,150 470,106 587,88 704,97 822,71" fill="none" stroke="var(--apps-line)" stroke-width="1.3"/>
        <path d="M0 159L117 193L235 185L352 159L470 176L587 167L704 140L822 115L822 264L0 264Z" fill="var(--goals-fill)"/>
        <polyline points="0,159 117,193 235,185 352,159 470,176 587,167 704,140 822,115" fill="none" stroke="var(--goals-line)" stroke-width="1.3"/>
        <g fill="#fff" stroke="var(--apps-line)" stroke-width="1.6">
          <circle cx="1" cy="150" r="5"/><circle cx="117" cy="167" r="5"/><circle cx="235" cy="167" r="5"/><circle cx="352" cy="150" r="5"/><circle cx="470" cy="106" r="5"/><circle cx="587" cy="88" r="5"/><circle cx="704" cy="97" r="5"/><circle cx="821" cy="71" r="5"/>
        </g>
        <g fill="#fff" stroke="var(--goals-line)" stroke-width="1.6">
          <circle cx="1" cy="159" r="5"/><circle cx="117" cy="193" r="5"/><circle cx="235" cy="185" r="5"/><circle cx="352" cy="159" r="5"/><circle cx="470" cy="176" r="5"/><circle cx="587" cy="167" r="5"/><circle cx="704" cy="140" r="5"/><circle cx="821" cy="115" r="5"/>
        </g>
      </svg>
      <div class="legend">
        <div><span style="background:var(--apps-line)"></span>Appearances</div>
        <div><span style="background:var(--goals-line)"></span>Goals</div>
      </div>
    </div>
  </section>
</main>

</body>
</html>
```